Marcus Tellow album cover "Borrowed Lanterns, Quiet Harbors"

3000x3000 album cover using attached image and provided text needed for cover of upcoming album for Seattle musician. Only front cover needed at this time.

Font styles to use
Serif
Sans Serif

Colors

Designer to choose colors to be used in the design.

```html
<!DOCTYPE html>
<html lang="en">
<head>
<meta charset="utf-8">
<title>Marcus Tellow – Borrowed Lanterns, Quiet Harbors</title>
<link rel="stylesheet" href="https://fonts.googleapis.com/css2?family=Bebas+Neue&family=Oswald:wght@300;400&display=swap">
<style>
  :root {
    --page: #f4f4f2;
    --cover-black: #0b0b0c;
    --cover-ink: #161618;
    --title-white: #ffffff;
    --accent-gold: #f2a534;
    --line-white: rgba(255, 255, 255, 0.92);
    --scene-sky: #2a3326;
    --scene-lit: #8a8560;
    --scene-lawn: #6f7a3c;
    --scene-shadow: #2b2a22;
  }
  * { margin: 0; padding: 0; box-sizing: border-box; }
  html, body {
    width: 1200px;
    height: 1152px;
    overflow: hidden;
    background: var(--page);
  }
  .album-cover {
    position: absolute;
    left: 50px;
    top: 26px;
    width: 1100px;
    height: 1100px;
    background: radial-gradient(ellipse at 50% 40%, var(--cover-ink) 0%, var(--cover-black) 70%);
    overflow: hidden;
  }
  .album-cover svg {
    position: absolute;
    inset: 0;
    width: 1100px;
    height: 1100px;
  }
  .artist-name {
    font-family: "Bebas Neue", "Oswald", sans-serif;
    fill: var(--title-white);
    font-size: 236px;
  }
  .album-title {
    font-family: "Oswald", sans-serif;
    font-weight: 300;
    font-size: 34px;
    letter-spacing: 1px;
    fill: var(--title-white);
  }
  .album-title .accent { fill: var(--accent-gold); font-weight: 400; }
  .frame-line {
    stroke: var(--line-white);
    stroke-width: 3;
    fill: none;
  }
</style>
</head>
<body>
  <main class="album-cover">
    <svg viewBox="0 0 1100 1100" xmlns="http://www.w3.org/2000/svg">
      <defs>
        <linearGradient id="scene-tone" x1="0" y1="0" x2="0" y2="1">
          <stop offset="0" stop-color="var(--scene-sky)"/>
          <stop offset="0.38" stop-color="var(--scene-lit)"/>
          <stop offset="0.7" stop-color="var(--scene-lawn)"/>
          <stop offset="1" stop-color="var(--scene-shadow)"/>
        </linearGradient>
      </defs>

      <path class="cover-photo" role="img"
            aria-label="Photograph: a vintage camper trailer lit up at night in a backyard with trees and lawn"
            fill="url(#scene-tone)"
            d="M 230 330
               C 250 240, 380 205, 520 215
               C 680 205, 840 240, 880 330
               C 910 420, 880 520, 820 610
               C 760 720, 650 800, 600 880
               C 575 925, 555 960, 537 985
               C 515 955, 490 915, 455 880
               C 380 810, 290 730, 240 620
               C 205 540, 205 420, 230 330 Z"/>

      <text class="artist-name" x="550" y="258" text-anchor="middle"
            textLength="900" lengthAdjust="spacingAndGlyphs">MARCUS TELLOW</text>

      <g class="frame-lines">
        <line class="frame-line" x1="109" y1="270" x2="522" y2="1020"/>
        <line class="frame-line" x1="1003" y1="268" x2="540" y2="1020"/>
        <polyline class="frame-line" points="470,918 537,978 600,918"/>
        <polyline class="frame-line" points="505,935 537,962 566,935"/>
      </g>

      <text class="album-title" x="79" y="1047">
        <tspan class="accent">BORROWED</tspan> LANTERNS
      </text>
      <text class="album-title" x="1010" y="1047" text-anchor="end">
        <tspan class="accent">QUIET</tspan> HARBORS
      </text>
    </svg>
  </main>
</body>
</html>
```